Verantu Mezcal needs a bottle design

We are a new brand of Mezcal in México, the name is Verantu Mezcal, and is based on our country´s moderns traditions. We would like to keep the black and white style. We also like to see on this bottle some minimalist icon about an agave or something that represents the Mexican culture. The product comes from a very outcast place, it comes from Durango, Mexico; Durango is a dry place with red soil and a lot of iron.

Important points:
*the bottle needs to keep a part of the neck uncovered, it doesn't need to be all the neck, but it needs to be on the neck (transparent to see the liquor).
*the main color has to be black or white (not necessarily both colors).
*the name´s font for ``VERANTU MEZCAL´´ is Lombok
* Black and withe colors only.
*the bottle needs to have ``VERANTU´´ and then ``MEZCAL´´, it cannot be ``MEZCAL VERANTU´´.
*the name ``MEZCAL´´ has to be smaller than ``VERANTU´´.Example: observe other alcoholic bottles like GLASSMERE vodka, the name ''GLASSMERE'' is bigger and gains more attention than ''vodka''.
* minimalist icon about an agave and/or something that represents the Mexican people or culture.

Bottle´s features:
Name: real
height: 12.090''
maximum width (top below the neck): 2.985''
minimum width (bottom): 2.798''
capacity: 750 ml.

Related concepts with our brand:
-class and style
-best traditional taste
-strong taste
-purity
-exclusive
-hard work
-appreciate the moments
-enjoy the time
-this is everything
-combination between city and villages

i will add the bottle specifications and the bottle we have now, we are looking something similar with the previous descriptions.

Target Market(s)

Male and Female of 20-50 years
you can find us on instagram or Facebook as Verantu Mezcal

Font styles to use
Other font styles liked:
• Lombok

Colors
ffffff
000000
1b1b1b

Requirements
Must have
• the name of the mezcal ''VERANTU'', and the name ''MEZCAL'' below the name ''VERANTU'' on the design
• it also has to have ''artesanal'' on the bottle, i will add the design we have.
Nice to have
• another symbol that represents the culture of México and its people. (something minimalistic)
Should not have
• to much colors
• Its NOT a tequila

```html
<!DOCTYPE html>
<html lang="en">
<head>
<meta charset="utf-8">
<title>Verantu Mezcal – Bottle</title>
<link rel="stylesheet" href="https://fonts.googleapis.com/css2?family=Josefin+Sans:wght@300;400&family=Roboto+Slab:wght@700&family=Arimo:wght@700&display=swap">
<style>
  :root {
    --backdrop: #d9d9d9;
    --ink: #000000;
    --charcoal: #1b1b1b;
    --paper: #e9e8f7;
    --white: #ffffff;
    --glass: #f2f2f2;
    --edge: #9a9a9a;
  }
  html, body {
    margin: 0;
    padding: 0;
    width: 1200px;
    height: 1000px;
    overflow: hidden;
    background: var(--backdrop);
  }
  .canvas {
    width: 1200px;
    height: 1000px;
    display: block;
  }
  .brand-name {
    font-family: "Josefin Sans", sans-serif;
    font-weight: 300;
    font-size: 44px;
    fill: var(--white);
  }
  .category {
    font-family: "Josefin Sans", sans-serif;
    font-weight: 300;
    font-size: 22px;
    letter-spacing: 1px;
    fill: var(--white);
  }
  .style-joven {
    font-family: "Roboto Slab", serif;
    font-weight: 700;
    font-size: 15px;
    fill: var(--ink);
  }
  .style-artesanal {
    font-family: "Josefin Sans", sans-serif;
    font-weight: 300;
    font-size: 30px;
    fill: var(--ink);
  }
  .volume {
    font-family: "Roboto Slab", serif;
    font-weight: 700;
    fill: var(--ink);
  }
  .agave-note {
    font-family: "Arimo", sans-serif;
    font-weight: 700;
    font-size: 12px;
    fill: var(--ink);
  }
</style>
</head>
<body>
<svg class="canvas" viewBox="0 0 1200 1000" xmlns="http://www.w3.org/2000/svg">
  <defs>
    <clipPath id="bottle-body">
      <path d="M567 42 H599 V250 C599 300 700 305 700 345 V972 Q700 985 688 985 H525 Q513 985 513 972 V345 C513 305 567 300 567 250 Z"/>
    </clipPath>
    <linearGradient id="motif-tone" x1="0" y1="1" x2="1" y2="0">
      <stop offset="0" stop-color="#000000"/>
      <stop offset="0.5" stop-color="#1b1b1b"/>
      <stop offset="1" stop-color="#000000"/>
    </linearGradient>
  </defs>

  <!-- cap -->
  <rect class="cap" x="562" y="12" width="41" height="32" rx="5" fill="var(--white)" stroke="#bdbdbd" stroke-width="1"/>

  <g clip-path="url(#bottle-body)">
    <!-- clear glass window on neck -->
    <rect class="neck-window" x="500" y="42" width="220" height="34" fill="var(--glass)"/>
    <!-- black upper label -->
    <rect class="label-dark" x="500" y="76" width="220" height="520" fill="var(--ink)"/>
    <!-- light lower label -->
    <polygon class="label-light" points="500,570 700,545 720,545 720,1000 500,1000" fill="var(--paper)"/>

    <!-- stair grid lines between bands -->
    <g class="stair-lines" stroke="var(--ink)" stroke-width="2">
      <line x1="650" y1="572" x2="650" y2="601"/>
      <line x1="680" y1="553" x2="680" y2="574"/>
      <line x1="550" y1="739" x2="550" y2="798"/>
      <line x1="600" y1="693" x2="600" y2="752"/>
      <line x1="650" y1="647" x2="650" y2="706"/>
      <line x1="560" y1="835" x2="560" y2="889"/>
      <line x1="610" y1="789" x2="610" y2="843"/>
      <line x1="660" y1="743" x2="660" y2="797"/>
    </g>

    <!-- diagonal bands carrying the agave / culture icon row -->
    <g class="motif-bands" role="img" aria-label="Diagonal black bands holding a repeated small white minimalist Mexican culture icon">
      <line x1="480" y1="780" x2="720" y2="560" stroke="url(#motif-tone)" stroke-width="34"/>
      <line x1="480" y1="885" x2="720" y2="665" stroke="url(#motif-tone)" stroke-width="34"/>
      <line x1="480" y1="985" x2="720" y2="765" stroke="url(#motif-tone)" stroke-width="34"/>
    </g>
  </g>

  <!-- outer glass edge -->
  <path class="bottle-outline" d="M567 42 H599 V250 C599 300 700 305 700 345 V972 Q700 985 688 985 H525 Q513 985 513 972 V345 C513 305 567 300 567 250 Z" fill="none" stroke="var(--edge)" stroke-width="1"/>

  <!-- name block -->
  <text class="brand-name" x="607" y="445" text-anchor="middle" textLength="182" lengthAdjust="spacingAndGlyphs">VERANTU</text>
  <line class="name-rule" x1="556" y1="493" x2="654" y2="493" stroke="var(--white)" stroke-width="1.5"/>
  <text class="category" x="605" y="540" text-anchor="middle">MEZCAL</text>

  <!-- style marks, set along the band direction -->
  <g transform="translate(534 674) rotate(-42)">
    <text class="style-joven" x="0" y="0">JOVEN</text>
  </g>
  <g transform="translate(524 712) rotate(-42)">
    <text class="style-artesanal" x="0" y="0">Artesanal</text>
  </g>

  <!-- volume and agave note -->
  <text class="volume" x="578" y="948"><tspan font-size="12">Net. </tspan><tspan font-size="20">750 ml</tspan></text>
  <text class="agave-note" x="612" y="972" text-anchor="middle">100% Agave Conizo</text>
</svg>
</body>
</html>
```